Local Chiropractor Needs Up Scale Webdesign

This website needs to have an upscale look with a very modern feel. Below is the information and websites to reference

Add Logo that is attached

Build a color scheme similar to this website image titled "chiro-1"

Must Include these pages in a horizontal menu bar in this order:
Home, Meet Our Staff, Patient Testimonials, Videos, Work Place Wellness, Contact

Build a "classy looking" Make An Appointment Button into the header with the contact info below

Phone Number:
555-314-2760

Address:
4182 Maple Fern Court, #305
Chanhassen, MN 55492

This website needs 4 rotating banners. Please reference a layout similar to this for the banners: http://drkelrom.com/. However design it nicer than this website, this website is very boring and doesn't flow with the colors properly

Below are the description for each banner

Rotating Banner #1
Use Image: Pediatrics
Two lines of text. First line title line, second description. Use Latin text for fill

Rotating Banner #2
Use Image: Aging Gracefully

Rotating Banner #3
Use Image: Pregnancy

Rotating Banner #4
Use Image: Athletics

I'd like to see a free consultation box similar to the "chiro-1" image. Fields to include are: First Name, Last Name, Phone Number, Comments.

For the body, please fill it with latin text. Please design a professional body layout. You can include a box in the right column for the hours

Office Hours
Monday: 8:00-11:00, 2:00-5:00
Tuesday: 8:30-11:00, 2:00-5:30
Wednesday: 8:00-11:00, 2:00-5:00
Thursday: 10:00-12:00, 2:30-5:00
Friday: 8:00-10:00, 1:00-5:00
Saturday: Closed
Sunday: Closed

For the footer please design something similar to the: http://drkelrom.com/

Also include in the Footer: Powered by Brightpath Site Co

Chiropractor

```html
<!DOCTYPE html>
<html lang="en">
<head>
<meta charset="utf-8">
<title>Thriving Life Chiropractic Health Center</title>
<link rel="stylesheet" href="https://fonts.googleapis.com/css2?family=Lato:wght@400;700&family=Alex+Brush&display=swap">
<style>
:root{
  --green:#9dc63e;
  --green-dark:#7aa82a;
  --charcoal:#2f2f2f;
  --charcoal-2:#3a3a3a;
  --footer:#262626;
  --gold:#b27c10;
  --ink:#222;
  --muted:#444;
  --white:#fff;
  --footer-text:#f2f2f2;
}
*{box-sizing:border-box;margin:0;padding:0}
html,body{width:1200px;height:2237px;overflow:hidden}
body{position:relative;font-family:'Lato',sans-serif;color:var(--ink);background:var(--white)}
.abs{position:absolute}
.topbar{left:0;top:0;width:1200px;height:30px;background:var(--green);color:var(--charcoal);font-size:14px}
.topbar .item{position:absolute;top:7px;display:flex;align-items:center;gap:10px}
.topbar .social{position:absolute;right:124px;top:9px;display:flex;gap:10px}
.dot{width:12px;height:12px;border-radius:50%;background:var(--charcoal)}
.header{left:0;top:30px;width:1200px;height:124px;background:var(--charcoal)}
.brand{left:124px;top:70px;display:flex;align-items:center;gap:12px;font-size:30px;color:var(--green)}
.brand .mark{width:34px;height:34px;border-radius:50%;background:var(--green)}
.appt{left:857px;top:63px;width:219px;height:58px;border-radius:6px;background:linear-gradient(var(--green),var(--green-dark));color:var(--white);font-size:19px;line-height:20px;display:flex;align-items:center;gap:18px;padding-left:22px;box-shadow:inset 0 0 0 1px rgba(255,255,255,.35)}
.nav{left:0;top:154px;width:1200px;height:55px;background:var(--green)}
.nav ul{list-style:none;position:absolute;left:121px;top:0;display:flex;height:55px}
.nav li{font-size:16px;color:var(--ink);line-height:55px}
.nav li.active{background:var(--charcoal);color:var(--white);padding:0 16px}
.hero{left:0;top:209px;width:1200px;height:467px;background:linear-gradient(90deg,#e8e4df 0%,#f4f1ee 45%,#e9e6e2 75%,#dcd8d2 100%)}
.hero-box{left:124px;top:337px;width:396px;height:148px;background:rgba(60,60,60,.82);color:var(--white);padding:14px 18px}
.hero-box h1{font-weight:400;font-size:26px;padding-bottom:10px;border-bottom:1px solid rgba(255,255,255,.6);margin-bottom:14px}
.hero-box p{font-size:14px;line-height:18px}
.btn{background:var(--green);color:var(--charcoal);font-weight:700;display:flex;align-items:center;justify-content:center}
.learn{left:124px;top:503px;width:137px;height:40px;font-size:17px}
.welcome{left:124px;top:695px;font-family:'Alex Brush',cursive;font-weight:400;font-size:40px;color:var(--ink)}
.subtitle{left:126px;top:744px;font-size:17px;letter-spacing:7.4px;color:var(--muted)}
.photo-frame{left:124px;top:787px;width:300px;height:237px;background:var(--charcoal);padding:20px 17px}
.photo{width:100%;height:100%;background:linear-gradient(#cfe8f5 0%,#8fc7e0 50%,#e9dcc6 80%,#f2e9d9 100%)}
.tile{width:146px;height:110px;padding:20px 10px;font-size:12.5px;line-height:17px}
.tile h3{font-weight:400;font-size:16.5px;margin-bottom:6px;white-space:nowrap}
.tile.light{background:var(--green);color:var(--charcoal)}
.tile.dark{background:var(--charcoal);color:var(--white)}
.t1{left:442px;top:787px;border-radius:0 14px 0 14px}
.t2{left:604px;top:787px;border-radius:14px 0 14px 0}
.t3{left:442px;top:915px;border-radius:14px 0 14px 0}
.t4{left:604px;top:915px;border-radius:0 14px 0 14px}
.lead{left:124px;top:1050px;width:630px;font-weight:700;font-size:15px}
.para{left:124px;top:1088px;width:630px;font-size:12.5px;line-height:19px;color:var(--muted)}
.more{left:124px;top:1140px;font-weight:700;font-size:15px;display:flex;align-items:center;gap:8px}
.consult{left:775px;top:703px;width:301px;height:454px;background:var(--green);box-shadow:0 3px 4px rgba(0,0,0,.35)}
.consult .banner{position:absolute;left:0;top:0}
.consult .c1{position:absolute;top:6px;width:100%;text-align:center;font-size:13px;color:var(--charcoal)}
.consult .c2{position:absolute;top:24px;width:100%;text-align:center;font-size:22px;color:var(--white)}
.consult .c3{position:absolute;top:58px;width:100%;text-align:center;font-size:16px;color:var(--charcoal)}
.consult .panel{position:absolute;left:17px;top:102px;width:267px;height:340px;background:var(--charcoal-2)}
.consult h4{position:absolute;top:117px;width:100%;text-align:center;font-weight:400;font-size:18px;color:var(--white)}
.field{position:absolute;left:27px;width:248px;height:32px;border:1px solid #ddd;color:var(--white);font-size:12px;padding:8px}
.submit{left:27px;top:370px;width:111px;height:41px;font-size:16px;position:absolute}
.video{left:124px;top:1193px;width:463px;height:282px;background:linear-gradient(#dfe4e8 0%,#f3f5f7 40%,#e7ebee 100%)}
.video .bar{position:absolute;left:0;bottom:0;width:100%;height:24px;background:#1b1b1b}
.video .prog{position:absolute;left:0;bottom:24px;width:100%;height:4px;background:#555}
.video .prog i{display:block;width:88px;height:4px;background:#d92020}
.video .time{position:absolute;left:60px;bottom:6px;color:#ddd;font-size:9px}
.right-text{left:610px;top:1195px;width:466px;font-size:12.5px;line-height:17px;color:var(--muted)}
.checks{left:610px;top:1302px;display:grid;grid-template-columns:140px 92px 97px 100px;row-gap:10px;font-size:13px;color:var(--muted)}
.checks span{display:flex;align-items:center;gap:8px}
.testi{left:775px;top:1382px;width:301px;height:351px;background:var(--green);text-align:center}
.testi .avatar{position:absolute;left:103px;top:28px;width:96px;height:96px;border-radius:50%;border:3px solid var(--white);background:linear-gradient(#f2f2f2,#bfc3c8)}
.testi .quote{position:absolute;top:128px;width:100%;font-family:Georgia,serif;font-size:48px;line-height:48px;font-weight:700;color:var(--charcoal)}
.testi p{position:absolute;left:20px;top:178px;width:261px;font-size:12.5px;line-height:17px;color:var(--charcoal)}
.testi .rule{position:absolute;left:75px;top:248px;width:151px;height:1px;background:rgba(255,255,255,.7)}
.testi .name{position:absolute;top:265px;width:100%;font-size:19px;color:var(--charcoal)}
.testi .dots{position:absolute;top:310px;left:117px;display:flex;gap:14px}
.testi .dots i{width:12px;height:12px;border-radius:50%;background:var(--white)}
.testi .dots i.on{box-shadow:0 0 0 3px var(--green),0 0 0 4px var(--white)}
.staff-title{left:124px;top:1530px;font-size:25px;font-weight:400;color:var(--ink)}
.staff{top:1585px;width:137px;height:137px;border-radius:50%;border:2px solid var(--green);padding:3px}
.staff .ph{width:100%;height:100%;border-radius:50%;background:linear-gradient(#eceff2,#9ea5ad)}
.staff .ph.g1{background:linear-gradient(#c9d9a6,var(--green))}
.staff .lbl{position:absolute;top:47px;width:100%;left:0;text-align:center;color:var(--charcoal);font-size:16px}
.staff .icons{position:absolute;top:74px;left:48px;display:flex;gap:8px}
.staff .icons i{width:9px;height:9px;border-radius:50%;background:var(--charcoal)}
.footer{left:0;top:1761px;width:1200px;height:476px;background:var(--footer)}
.tab{top:1761px;width:476px;height:57px;font-size:24px;display:flex;align-items:center;justify-content:center;border-bottom:3px solid #e8e8e8}
.tab.biz{left:124px;background:var(--gold);color:var(--white)}
.tab.news{left:600px;background:var(--green);color:var(--charcoal)}
.ftitle{font-size:21px;font-weight:400;color:var(--white);padding-bottom:6px;border-bottom:1px solid #bbb;display:inline-block}
.contact{left:124px;top:1855px;color:var(--footer-text)}
.contact .row{display:flex;gap:12px;font-size:13.5px;line-height:22px;margin-top:18px}
.contact .row:first-of-type{margin-top:26px}
.map{left:369px;top:1861px;width:380px;height:254px;background:linear-gradient(135deg,#e9e6df,#d9d5cc)}
.hours{left:775px;top:1855px;width:301px;color:var(--footer-text)}
.hours table{width:100%;border-collapse:collapse;margin-top:6px;font-size:13.5px;color:var(--footer-text)}
.hours th{text-align:left;font-weight:400;font-size:17px;padding:8px 0;color:var(--white)}
.hours td{padding:8px 0;border-bottom:1px solid #8a8a8a}
.hours td:first-child,.hours th:first-child{width:92px}
.hours td:nth-child(2),.hours th:nth-child(2){width:106px}
.copy-rule{left:124px;top:2190px;width:952px;height:1px;background:#777}
.copy{left:0;top:2202px;width:1200px;text-align:center;font-size:13px;color:#ddd}
</style>
</head>
<body>

<div class="abs topbar">
  <div class="item" style="left:124px">
    <svg width="13" height="13" viewBox="0 0 24 24"><path fill="#2f2f2f" d="M6.6 10.8a15 15 0 0 0 6.6 6.6l2.2-2.2c.3-.3.7-.4 1-.2 1.1.4 2.3.6 3.6.6.6 0 1 .4 1 1V20c0 .6-.4 1-1 1C10.6 21 3 13.4 3 4c0-.6.4-1 1-1h3.5c.6 0 1 .4 1 1 0 1.3.2 2.5.6 3.6.1.3 0 .7-.2 1z"/></svg>
    555-314-2760
  </div>
  <div class="item" style="left:425px">
    <svg width="11" height="14" viewBox="0 0 24 30"><path fill="#2f2f2f" d="M12 0C5.4 0 0 5.3 0 11.8 0 20.6 12 30 12 30s12-9.4 12-18.2C24 5.3 18.6 0 12 0zm0 16a4.3 4.3 0 1 1 0-8.6 4.3 4.3 0 0 1 0 8.6z"/></svg>
    4182 Maple Fern Court, #305 Chanhassen, MN 55492
  </div>
  <div class="social"><i class="dot"></i><i class="dot"></i><i class="dot"></i><i class="dot"></i></div>
</div>

<header class="abs header"></header>
<div class="abs brand"><span class="mark"></span>Thriving Life</div>
<div class="abs appt">
  <svg width="30" height="36" viewBox="0 0 30 36"><rect x="2" y="5" width="26" height="29" rx="2" fill="#fff"/><rect x="2" y="5" width="26" height="7" fill="#e6e6e6"/><g stroke="#9dc63e" stroke-width="1.5"><line x1="6" y1="18" x2="24" y2="18"/><line x1="6" y1="23" x2="24" y2="23"/><line x1="6" y1="28" x2="24" y2="28"/></g><g fill="#888"><rect x="7" y="1" width="2" height="8"/><rect x="14" y="1" width="2" height="8"/><rect x="21" y="1" width="2" height="8"/></g></svg>
  <span>Make An<br>Appointment</span>
</div>

<nav class="abs nav">
  <ul>
    <li class="active">Home</li>
    <li style="margin-left:64px">Meet Our Staff</li>
    <li style="margin-left:84px">Patient Testimonials</li>
    <li style="margin-left:82px">Videos</li>
    <li style="margin-left:86px">Work Place Wellness</li>
    <li style="margin-left:78px">Contact</li>
  </ul>
</nav>

<div class="abs hero" role="img" aria-label="Photo of a young child gently touching a pregnant mother's belly"></div>
<div class="abs hero-box">
  <h1>Supporting Healthy Lifestyles</h1>
  <p>Lorem ipsum do sit amet, consectetuer adipiscing elit. Pat vestibulum molestie lacus. Aenean nodrerit mauris. Phasellus porta. Fusce susc varius mi</p>
</div>
<div class="abs btn learn">Learn More</div>

<h2 class="abs welcome">Wel come To Thriving Life !</h2>
<div class="abs subtitle">Chiropractic Health Center</div>

<div class="abs photo-frame"><div class="photo" role="img" aria-label="Photo of a family walking hand in hand along a beach"></div></div>
<div class="abs tile light t1"><h3>Pediatrics</h3>Lorem ipsum dolorS-esquamestqui dolor</div>
<div class="abs tile dark t2"><h3>Aging Gracefully</h3>Lorem ipsum dolorS-esquamestqui dolor</div>
<div class="abs tile dark t3"><h3>Pregnancy</h3>Lorem ipsum dolorS-esquamestqui dolor</div>
<div class="abs tile light t4"><h3>Athletics</h3>Lorem ipsum dolorS-esquamestqui dolor</div>

<p class="abs lead">Lorem ipsum dolor sit amet consect Caut oditau insentur magni dolquatio.</p>
<p class="abs para">Sesquam estqui dolorem ipsudolor sitamet conetasedas adipisci umquam eius.m aliqua quaerat ptatem. Sesquam estqui dolorem ipsudolor sitamet conetasedas adipisci umquam eius.</p>
<div class="abs more">READ MORE
  <svg width="16" height="10" viewBox="0 0 16 10"><path d="M0 5h13M9 1l4 4-4 4" stroke="#222" stroke-width="2" fill="none"/></svg>
</div>

<aside class="abs consult">
  <svg class="banner" width="301" height="110" viewBox="0 0 301 110"><path d="M0 0h301v72l-150 30L0 72z" fill="#8ab833"/><line x1="30" y1="66" x2="110" y2="66" stroke="#fff" stroke-width="1"/><line x1="191" y1="66" x2="271" y2="66" stroke="#fff" stroke-width="1"/></svg>
  <div class="c1">CONTACT US NOW AND GET YOUR</div>
  <div class="c2">FREE CONSULTATION</div>
  <div class="c3">TODAY</div>
  <div class="panel"></div>
  <h4>WELLNESS BEGINS HERE</h4>
  <div class="field" style="top:153px">First Name</div>
  <div class="field" style="top:197px">Last Name</div>
  <div class="field" style="top:241px">Phone Number</div>
  <div class="field" style="top:285px;height:75px">Comment</div>
  <div class="btn submit">Submit</div>
</aside>

<div class="abs video" role="img" aria-label="Video still of two skiers descending a snowy slope">
  <div class="prog"><i></i></div>
  <div class="bar"><span class="time">0:16 / 1:31</span></div>
</div>

<p class="abs right-text">Lorem ipsum do sit amet, consectetuer adipiscing elit. Pat vestibulum molestie lacus. Aenean nodrerit mauris. Phasellus porta. Fusce susc varius mi. Cum sociis natoque penatibumagnis dis parturient montes, nascetur ridiculus.Aenean nodrerit mauris. Phasellus porta. Fusce susc varius mi. Cum sociis natoque penatibumagnis dis parturient montes, nascetur ridiculus.</p>

<div class="abs checks">
  <span><svg width="12" height="12" viewBox="0 0 12 12"><circle cx="6" cy="6" r="6" fill="#333"/><path d="M5 3l3 3-3 3" stroke="#fff" stroke-width="1.6" fill="none"/></svg>Health</span>
  <span><svg width="12" height="12" viewBox="0 0 12 12"><circle cx="6" cy="6" r="6" fill="#333"/><path d="M5 3l3 3-3 3" stroke="#fff" stroke-width="1.6" fill="none"/></svg>Exercise</span>
  <span><svg width="12" height="12" viewBox="0 0 12 12"><circle cx="6" cy="6" r="6" fill="#333"/><path d="M5 3l3 3-3 3" stroke="#fff" stroke-width="1.6" fill="none"/></svg>Bacon</span>
  <span><svg width="12" height="12" viewBox="0 0 12 12"><circle cx="6" cy="6" r="6" fill="#333"/><path d="M5 3l3 3-3 3" stroke="#fff" stroke-width="1.6" fill="none"/></svg>Salami</span>
  <span><svg width="12" height="12" viewBox="0 0 12 12"><circle cx="6" cy="6" r="6" fill="#333"/><path d="M5 3l3 3-3 3" stroke="#fff" stroke-width="1.6" fill="none"/></svg>Roast &amp; Cooked</span>
  <span><svg width="12" height="12" viewBox="0 0 12 12"><circle cx="6" cy="6" r="6" fill="#333"/><path d="M5 3l3 3-3 3" stroke="#fff" stroke-width="1.6" fill="none"/></svg>Beef</span>
  <span><svg width="12" height="12" viewBox="0 0 12 12"><circle cx="6" cy="6" r="6" fill="#333"/><path d="M5 3l3 3-3 3" stroke="#fff" stroke-width="1.6" fill="none"/></svg>Smoked</span>
  <span><svg width="12" height="12" viewBox="0 0 12 12"><circle cx="6" cy="6" r="6" fill="#333"/><path d="M5 3l3 3-3 3" stroke="#fff" stroke-width="1.6" fill="none"/></svg>Specialties</span>
</div>

<aside class="abs testi">
  <div class="avatar" role="img" aria-label="Portrait photo of the patient giving the testimonial"></div>
  <div class="quote">&#8220;</div>
  <p>Sed in lacus ut enim adipiscing aliquet. Nulla venenatis. In pede mi, aliquet sit amet, euismod in, auctor ut, ligula. Aliquam dapibus tincidunt</p>
  <div class="rule"></div>
  <div class="name">June Harlow</div>
  <div class="dots"><i class="on"></i><i></i><i></i></div>
</aside>

<h2 class="abs staff-title">Meet Our Staff</h2>
<div class="abs staff" style="left:124px"><div class="ph g1" role="img" aria-label="Portrait photo of staff member Ana Corvel"></div><div class="lbl">Ana Corvel</div><div class="icons"><i></i><i></i><i></i></div></div>
<div class="abs staff" style="left:287px"><div class="ph" role="img" aria-label="Portrait photo of a male staff member"></div></div>
<div class="abs staff" style="left:450px"><div class="ph" role="img" aria-label="Portrait photo of a female staff member"></div></div>
<div class="abs staff" style="left:613px"><div class="ph" role="img" aria-label="Portrait photo of a male staff member"></div></div>

<footer class="abs footer"></footer>
<div class="abs tab biz">Business Information</div>
<div class="abs tab news">Newsletter</div>

<div class="abs contact">
  <h3 class="ftitle">Contact Us</h3>
  <div class="row"><svg width="11" height="14" viewBox="0 0 24 30" style="margin-top:4px"><path fill="#fff" d="M12 0C5.4 0 0 5.3 0 11.8 0 20.6 12 30 12 30s12-9.4 12-18.2C24 5.3 18.6 0 12 0zm0 16a4.3 4.3 0 1 1 0-8.6 4.3 4.3 0 0 1 0 8.6z"/></svg><span>4182 Maple Fern Court, #305<br>Chanhassen, MN 55492</span></div>
  <div class="row"><svg width="14" height="14" viewBox="0 0 24 24" style="margin-top:4px"><rect width="24" height="24" rx="4" fill="#fff"/><path fill="#262626" d="M7.5 11a11 11 0 0 0 5.5 5.5l1.6-1.6c.3-.3.6-.3.9-.2.8.3 1.7.4 2.5.4v3c0 .5-.3.8-.8.8C10.9 18.9 5.1 13.1 5.1 6.8c0-.5.3-.8.8-.8h3c0 .9.1 1.7.4 2.5.1.3 0 .6-.2.9z"/></svg><span>555-314-2760</span></div>
  <div class="row"><svg width="14" height="11" viewBox="0 0 24 18" style="margin-top:6px"><rect width="24" height="18" fill="#fff"/><path d="M0 0l12 9 12-9" stroke="#262626" stroke-width="2" fill="none"/></svg><span>hello@thrivinglifechiro.com</span></div>
</div>

<div class="abs map" role="img" aria-label="Street map showing the office location"></div>

<div class="abs hours">
  <h3 class="ftitle">Office Hours</h3>
  <table>
    <tr><th>Day</th><th>Hours</th><th></th></tr>
    <tr><td>Monday:</td><td>8:00-11:00</td><td>2pm - 5pm</td></tr>
    <tr><td>Tuesday:</td><td>8:30-11:00</td><td>2pm - 5:30pm</td></tr>
    <tr><td>Wednesday:</td><td>8:00-11:00</td><td>2pm - 5pm</td></tr>
    <tr><td>Thursday:</td><td>10:00-12:00</td><td>2:30pm - 5pm</td></tr>
    <tr><td>Friday:</td><td>8:00-10:00</td><td>1pm - 5pm</td></tr>
    <tr><td>Saturday:</td><td>Closed</td><td></td></tr>
    <tr><td>Sunday:</td><td>Closed</td><td></td></tr>
  </table>
</div>

<div class="abs copy-rule"></div>
<div class="abs copy">Copyright ©2015 thrivinglife. All Rights Reserved</div>

</body>
</html>
```